R & T Summit Construction Business Card ideas

We want a business card to represents our company in a way that looks professional but is also a business card that is unique!

Industry/Entity Type

Construction Company

Contact Information for Business Card

open to all design ideas, just want to be able to see different options to choose from in either color or grayscale.

Requirements
Must have
• Our names and phone numbers
• Nolan Pritchett 512-804-2271
• Curtis Hale 512-693-1804
• Business logo

```html
<!DOCTYPE html>
<html lang="en">
<head>
<meta charset="utf-8">
<title>R &amp; T Summit Construction – Business Card</title>
<link rel="stylesheet" href="https://fonts.googleapis.com/css2?family=Tinos:wght@400;700&family=Montserrat:wght@500&display=swap">
<style>
  :root {
    --backdrop: #f1f1f1;
    --ink: #0b0b0c;
    --paper: #fbfbfc;
    --light: #ffffff;
  }
  * { margin: 0; padding: 0; box-sizing: border-box; }
  html, body { width: 1200px; height: 1000px; overflow: hidden; }
  body { background: var(--backdrop); position: relative; }

  .card {
    position: absolute;
    width: 478px;
    height: 273px;
    border-radius: 24px;
    overflow: hidden;
  }
  .card--front { left: 169px; top: 200px; background: var(--paper); }
  .card--back  { left: 552px; top: 570px; background: var(--ink); }

  .brand-name {
    position: absolute;
    left: 0; right: 0;
    text-align: center;
    font-family: "Tinos", "Times New Roman", serif;
    font-weight: 700;
    font-size: 23px;
    line-height: 30px;
    letter-spacing: 0.3px;
  }
  .card--front .brand-name { top: 78px; color: var(--ink); }
  .card--back  .brand-name { top: 120px; color: var(--light); }

  .contact-band {
    position: absolute;
    left: 0; right: 0; top: 214px; bottom: 0;
    background: var(--ink);
  }
  .band-rule {
    position: absolute;
    left: 0; right: 0; top: 209px;
    height: 2px;
    background: var(--ink);
  }

  .person {
    position: absolute;
    top: 170px;
    width: 160px;
    text-align: center;
  }
  .person--left  { left: 6px; }
  .person--right { left: 312px; }

  .person__name {
    font-family: "Tinos", "Times New Roman", serif;
    font-size: 19px;
    color: var(--ink);
    line-height: 24px;
    white-space: nowrap;
  }
  .person__icon {
    display: block;
    margin: 3px auto 0;
    width: 32px;
    height: 32px;
  }
  .person__phone {
    margin-top: 6px;
    font-family: "Montserrat", Arial, sans-serif;
    font-weight: 500;
    font-size: 12px;
    color: var(--light);
    letter-spacing: 0.4px;
  }
</style>
</head>
<body>

  <section class="card card--front" aria-label="Business card front">
    <p class="brand-name">R &amp; T Summit Construction</p>

    <div class="band-rule"></div>
    <div class="contact-band"></div>

    <div class="person person--left">
      <p class="person__name">Nolan Pritchett</p>
      <svg class="person__icon" viewBox="0 0 32 32" aria-hidden="true">
        <circle cx="16" cy="16" r="14.5" fill="#fff" stroke="#0b0b0c" stroke-width="2"/>
        <path d="M9 14c0-2 3-3 7-3s7 1 7 3l-2 1.5-2-1v-1.5h-6v1.5l-2 1z" fill="#0b0b0c"/>
        <path d="M11.5 16h9l1.5 5h-12z" fill="#0b0b0c"/>
        <circle cx="16" cy="18.5" r="1.3" fill="#fff"/>
      </svg>
      <p class="person__phone">512-804-2271</p>
    </div>

    <div class="person person--right">
      <p class="person__name">Curtis Hale</p>
      <svg class="person__icon" viewBox="0 0 32 32" aria-hidden="true">
        <circle cx="16" cy="16" r="14.5" fill="#fff" stroke="#0b0b0c" stroke-width="2"/>
        <path d="M9 14c0-2 3-3 7-3s7 1 7 3l-2 1.5-2-1v-1.5h-6v1.5l-2 1z" fill="#0b0b0c"/>
        <path d="M11.5 16h9l1.5 5h-12z" fill="#0b0b0c"/>
        <circle cx="16" cy="18.5" r="1.3" fill="#fff"/>
      </svg>
      <p class="person__phone">512-693-1804</p>
    </div>
  </section>

  <section class="card card--back" aria-label="Business card back">
    <p class="brand-name">R &amp; T Summit Construction</p>
  </section>

</body>
</html>
```